Awesome photographers card for an awesome new business

Double sided business card Black background and silver logo in middle on one side. Details on otherside. please keep it simple

Photographer

Gavin Tolley
0482615073
GavinTolleyPhotography82@lumenpost.com
www.GavinTolleyPhotography.com.au
Instagram _Gavin_tolley

Requirements
Must have
• My logo in Silver
• please use instagram logo instead of "Instagram"

```html
<!DOCTYPE html>
<html lang="en">
<head>
<meta charset="utf-8">
<title>Gavin Tolley Photography – Business Card</title>
<link href="https://fonts.googleapis.com/css2?family=Allura&family=Lato:wght@300;400&display=swap" rel="stylesheet">
<style>
  :root {
    --page: #ffffff;
    --card: #060606;
    --card-glow: #2a2a2a;
    --silver: #d9dbde;
    --grey-text: #a9abae;
    --shadow: rgba(0,0,0,0.45);
  }
  * { margin: 0; padding: 0; box-sizing: border-box; }
  html, body {
    width: 1200px; height: 1200px; overflow: hidden;
    background: var(--page);
  }
  .sheet { position: relative; width: 1200px; height: 1200px; }
  .card {
    position: absolute; left: 320px; width: 560px; height: 320px;
    background: var(--card); overflow: hidden;
    box-shadow: 2px 2px 3px var(--shadow);
  }
  .card--front { top: 246px; }
  .card--back { top: 648px; }
  .card__backdrop { position: absolute; inset: 0; }
  .card--front .card__backdrop {
    background:
      radial-gradient(ellipse 70% 30% at 60% 88%, var(--card-glow), transparent 70%),
      var(--card);
  }
  .card--back .card__backdrop {
    background:
      radial-gradient(ellipse 75% 30% at 45% 8%, var(--card-glow), transparent 70%),
      var(--card);
  }
  .brand-mark {
    position: absolute; left: 212px; top: 100px; width: 136px; height: 136px;
    border: 2px solid var(--silver); border-radius: 50%;
    display: flex; align-items: center; justify-content: center;
  }
  .brand-mark__name {
    font-family: "Lato", sans-serif; font-weight: 400; font-size: 13px;
    letter-spacing: 3px; text-transform: uppercase; color: var(--silver);
    text-align: center; line-height: 1.5;
  }
  .details {
    position: absolute; inset: 0; text-align: center; color: var(--silver);
    font-family: "Lato", sans-serif;
  }
  .details__name {
    position: absolute; left: 0; right: 0; top: 74px;
    font-family: "Allura", cursive; font-size: 36px; font-weight: 400;
    letter-spacing: 2px; color: #f2f2f2;
  }
  .details__role {
    position: absolute; left: 0; right: 0; top: 123px;
    font-size: 12px; font-weight: 300; letter-spacing: 5px; color: var(--grey-text);
  }
  .details__phone {
    position: absolute; left: 0; right: 0; top: 158px;
    font-size: 11.5px; font-weight: 400; letter-spacing: 1px;
  }
  .details__contact {
    position: absolute; left: 0; right: 0; top: 232px;
    list-style: none; font-size: 11.5px; font-weight: 400; line-height: 23px;
  }
  .details__web { letter-spacing: 0.8px; }
  .details__social-mark {
    display: inline-block; width: 9px; height: 9px; border: 1px solid var(--silver);
    border-radius: 2px; margin-right: 3px; vertical-align: -0.5px;
  }
</style>
</head>
<body>
<main class="sheet">
  <section class="card card--front" aria-label="Card front">
    <div class="card__backdrop" role="img" aria-label="Soft silver light streaks on black"></div>
    <div class="brand-mark">
      <p class="brand-mark__name">Gavin<br>Tolley</p>
    </div>
  </section>

  <section class="card card--back" aria-label="Card back">
    <div class="card__backdrop" role="img" aria-label="Soft silver light streaks on black"></div>
    <div class="details">
      <h1 class="details__name">Gavin Tolley</h1>
      <p class="details__role">PHOTOGRAPHER</p>
      <p class="details__phone">0482 615 073</p>
      <ul class="details__contact">
        <li class="details__email">GavinTolleyPhotography82@lumenpost.com</li>
        <li class="details__social"><span class="details__social-mark"></span>Gavin_Tolley</li>
        <li class="details__web">www.GavinTolleyPhotography.com.au</li>
      </ul>
    </div>
  </section>
</main>
</body>
</html>
```